Business card design needed

I have a leadership coaching and consultancy business which specialises in the education sector. I would like a clean, professional design). The design needs to speak to strength, support, new learning, connections & a growth mindest.

I am also looking for a unique LOGO. This is very important.

Target Market(s)

Educational Leaders & executives

Industry/Entity Type

Leadership

Contact Information for Business Card

Miranda Voss
Principal Coach & Consultant
Miranda Voss Coaching & Consulting
0491 362 815
miranda.voss@quillmail.example
I also would like my facebook, twitter and linkedin accounts to appear

Logo styles of interest
Lettermark Logo
Requirements
Must have
• A 2 sided business card with contact details on the back
A logo

```html
<!DOCTYPE html>
<html lang="en">
<head>
<meta charset="utf-8">
<title>Miranda Voss – Business Card</title>
<link rel="stylesheet" href="https://fonts.googleapis.com/css2?family=Sofia&family=Rokkitt:wght@400&family=Sorts+Mill+Goudy&display=swap">
<style>
  :root {
    --sun: #F0BD42;
    --tangerine: #F28C33;
    --plum: #35124F;
    --violet: #6A3A86;
    --lilac: #8B6E9E;
    --band-text: #F2963A;
    --circle-orange: #F29A12;
  }
  * { margin: 0; padding: 0; box-sizing: border-box; }
  html, body { width: 1200px; height: 692px; overflow: hidden; background: var(--sun); }
  .card { position: relative; width: 1200px; height: 692px; background: var(--sun); overflow: hidden; }

  .name {
    position: absolute; left: 78px; top: 40px;
    font-family: "Sofia", cursive; font-size: 112px; line-height: 1;
    color: var(--plum); white-space: nowrap;
  }
  .role-band {
    position: absolute; left: 82px; top: 238px; width: 773px; height: 49px;
    background: var(--plum);
    display: flex; align-items: center; justify-content: center;
  }
  .role {
    font-family: "Rokkitt", serif; font-size: 37px; letter-spacing: 1.5px;
    color: var(--band-text); white-space: nowrap;
  }
  .company {
    position: absolute; left: 80px; top: 350px;
    font-family: "Sofia", cursive; font-size: 60px; line-height: 1;
    color: var(--violet); white-space: nowrap;
  }

  .mark-top { position: absolute; left: 920px; top: 40px; width: 180px; text-align: center; }
  .mark-top svg { display: block; margin: 0 auto; }
  .mark-top .mark-name {
    font-family: "Sorts Mill Goudy", serif; font-size: 24px; color: var(--plum); margin-top: 8px;
  }

  .contact-strip {
    position: absolute; left: 0; top: 503px; width: 1200px; height: 189px;
    background: var(--tangerine); border-top: 3px solid var(--plum);
  }
  .phone {
    position: absolute; left: 60px; top: 22px;
    font-family: "Sorts Mill Goudy", serif; font-size: 50px; color: var(--plum); white-space: nowrap;
  }
  .email {
    position: absolute; left: 60px; top: 118px;
    font-family: "Sorts Mill Goudy", serif; font-size: 32px; color: var(--violet); white-space: nowrap;
  }
  .mark-bottom {
    position: absolute; left: 560px; top: 58px; width: 170px;
    display: flex; align-items: center; gap: 8px;
  }
  .mark-bottom .mark-name {
    font-family: "Sorts Mill Goudy", serif; font-size: 18px; color: var(--plum); white-space: nowrap;
  }
  .social {
    position: absolute; right: 63px; top: 18px; list-style: none; text-align: right;
    font-family: "Sorts Mill Goudy", serif; font-size: 32px; line-height: 50px;
  }
  .social .facepage, .social .linkedpro { color: var(--plum); }
  .social .chirper { color: var(--lilac); }
</style>
</head>
<body>
<main class="card">
  <h1 class="name">Miranda Voss</h1>
  <div class="role-band"><p class="role">PRINCIPAL COACH &amp; CONSULTANT</p></div>
  <p class="company">Miranda Voss Coaching &amp; Consulting</p>

  <div class="mark-top">
    <svg width="150" height="150" viewBox="0 0 150 150" aria-hidden="true">
      <circle cx="75" cy="75" r="72" fill="var(--circle-orange)" opacity="0.85"/>
    </svg>
    <p class="mark-name">Miranda Voss</p>
  </div>

  <section class="contact-strip">
    <p class="phone">Tel. 0491 362 815</p>
    <p class="email">miranda.voss@quillmail.example</p>

    <div class="mark-bottom">
      <svg width="60" height="60" viewBox="0 0 60 60" aria-hidden="true">
        <circle cx="30" cy="30" r="28" fill="var(--plum)" opacity="0.7"/>
      </svg>
      <span class="mark-name">Miranda Voss</span>
    </div>

    <ul class="social">
      <li class="facepage">facepage/miranda.voss</li>
      <li class="chirper">chirper: @mirandavoss</li>
      <li class="linkedpro">linkedpro/miranda.voss</li>
    </ul>
  </section>
</main>
</body>
</html>
```